Onboarding project UI redesign

The web site is used to onboard clients via a video-identification process.
The end-user first tests his computer, then enters his order details and waits for an operator engagement.
When the operator engages the customer, they go through some identification steps together, ending on a contract signature page.

Target Market(s)

Finance B2C

Industry/Entity Type

Finance

Font styles to use
Sans Serif

Requirements
Must have
• Professional UI
• Design for mobile devices

```html
<!DOCTYPE html>
<html lang="en">
<head>
<meta charset="utf-8">
<title>Novara Bank – Video identification</title>
<link rel="stylesheet" href="https://fonts.googleapis.com/css2?family=Rubik:wght@400;500&display=swap">
<style>
  :root {
    --brand-blue: #1f4e8c;
    --step-bg: #e4e7eb;
    --step-text: #3e6496;
    --title-text: #333a40;
    --muted-text: #7d8a99;
    --footer-bg: #e3e6e9;
    --confirm-green: #2eaa8a;
    --white: #ffffff;
    --video-base: #d9d4cc;
  }
  * { box-sizing: border-box; margin: 0; padding: 0; }
  html, body { width: 1200px; height: 864px; overflow: hidden; }
  body {
    position: relative;
    background: var(--white);
    font-family: "Rubik", Arial, sans-serif;
  }
  .site-header {
    position: absolute; left: 0; top: 0;
    width: 1200px; height: 129px;
    background: var(--brand-blue);
    display: flex; align-items: center; justify-content: center;
  }
  .brand-name {
    color: var(--white);
    font-size: 22px; font-weight: 400;
    letter-spacing: 0.5px;
  }
  .step-badge {
    position: absolute; left: 534px; top: 169px;
    width: 131px; height: 38px;
    background: var(--step-bg);
    border-radius: 3px;
    color: var(--step-text);
    font-size: 13px; letter-spacing: 1.6px;
    display: flex; align-items: center; justify-content: center;
  }
  .page-title {
    position: absolute; left: 0; top: 238px; width: 1200px;
    text-align: center;
    color: var(--title-text);
    font-size: 25.5px; font-weight: 400;
  }
  .recording-frame {
    position: absolute; left: 157px; top: 317px;
    width: 454px; height: 369px;
    border: 2.5px solid var(--brand-blue);
    border-radius: 7px;
  }
  .recording-label {
    position: absolute; left: 18px; top: -8px;
    padding: 0 14px;
    background: var(--white);
    color: var(--brand-blue);
    font-size: 11.5px; font-weight: 500; letter-spacing: 1.2px;
    line-height: 14px;
  }
  .video-feed {
    position: absolute; left: 9px; top: 14px;
    width: 432px; height: 340px;
    border-radius: 7px;
    background: linear-gradient(160deg, #ebe7e1 0%, var(--video-base) 55%, #a9b6c6 100%);
  }
  .self-view {
    position: absolute; left: 304px; top: 0;
    width: 109px; height: 126px;
    border: 1.5px solid var(--brand-blue);
    border-top: none;
    background: linear-gradient(170deg, #e6e4e2 0%, #c9c7c4 60%, #8fa3bd 100%);
  }
  .instructions {
    position: absolute; left: 688px; top: 332px;
    width: 360px;
    color: var(--muted-text);
    font-size: 14px; line-height: 21px;
  }
  .action-bar {
    position: absolute; left: 0; top: 752px;
    width: 1200px; height: 112px;
    background: var(--footer-bg);
  }
  .confirm-button {
    position: absolute; left: 898px; top: 37px;
    width: 146px; height: 38px;
    border: none; border-radius: 19px;
    background: var(--confirm-green);
    color: var(--white);
    font-family: "Rubik", Arial, sans-serif;
    font-size: 13px; font-weight: 500; letter-spacing: 1.4px;
  }
</style>
</head>
<body>
  <header class="site-header">
    <span class="brand-name">NOVARA BANK</span>
  </header>

  <div class="step-badge">STEP&nbsp; 1 / 11</div>

  <h1 class="page-title">Confirm quality of connection and communication</h1>

  <section class="recording-frame">
    <span class="recording-label">RECORDING</span>
    <div class="video-feed" role="img" aria-label="Live webcam video of the customer">
      <div class="self-view" role="img" aria-label="Small self-view preview of the customer's camera"></div>
    </div>
  </section>

  <p class="instructions">In order to complete this process, keep your identity document ready.</p>

  <footer class="action-bar">
    <button class="confirm-button">CONFIRM</button>
  </footer>
</body>
</html>
```